Pelterane Aviation - Insurance Brokers - Half page magazine ad.

Half-page ad in an aviation industry magazine promoting our services as an aviation insurance broker. I've attached an example of a pop-up banner we used at a conference recently to give you an idea.

I have attached a copy of the specifications from the publisher. Half-page ad requires:
- 190mm width x 132mm height
- Minimum 300 dpi
- colours in CMYK
- high resolution PDF with fonts embedded

Target Market(s)

Aircraft owners/operators, drone owners/operators, pilots

Font styles to use
Serif

Colors

Designer to choose colors to be used in the design.

Requirements
Must have
• 1. Company logo (attached).
• 2. Contact Details as follows:
• www.qmvaviation.com.au
• (02) 4931 7262
Nice to have
• Maybe a picture of an aircraft/helicopter in the bakground with logo/text etc over the top. But happy to look at alternative design options.

```html
<!DOCTYPE html>
<html lang="en">
<head>
<meta charset="utf-8">
<title>Pelterane Aviation – Half Page Ad Options</title>
<link rel="stylesheet" href="https://fonts.googleapis.com/css2?family=Mulish:wght@400;600;800;900&display=swap">
<style>
  :root{
    --brand-red:#c8153f;
    --brand-red-dark:#9c1730;
    --brand-blue:#123a8c;
    --accent-pink:#e8467a;
    --ink-dark:#1d1d1f;
    --white:#ffffff;
    --board-top:#7b7b7b;
    --board-bottom:#3c3c3c;
  }
  *{margin:0;padding:0;box-sizing:border-box}
  html,body{width:854px;height:1200px;overflow:hidden}
  body{
    position:relative;
    background:linear-gradient(180deg,var(--board-top),var(--board-bottom));
    font-family:"Mulish",sans-serif;
  }
  .ad-frame{position:absolute;left:60px;width:734px;height:509px;overflow:hidden;box-shadow:0 4px 14px rgba(0,0,0,.35)}
  .ad-frame--one{top:50px}
  .ad-frame--two{top:618px}
  .ad{position:absolute;left:0;top:0;width:917px;height:636px;transform:scale(.8);transform-origin:0 0;background:var(--white)}
  .ad__bg{position:absolute;inset:0;width:917px;height:636px}
  .option-label{position:absolute;left:0;width:854px;text-align:center;color:var(--white);font-size:21px;font-weight:400}
  .option-label--one{top:572px}
  .option-label--two{top:1144px}

  .brand{position:absolute;left:50px;top:40px;display:flex;align-items:center;gap:12px}
  .brand__mark{width:26px;height:26px;background:var(--brand-blue)}
  .brand__name{font-size:36px;font-weight:900;color:var(--brand-blue);letter-spacing:-.5px}

  .phone{position:absolute;left:490px;top:19px;height:62px;display:flex;align-items:center;gap:12px}
  .phone__icon{width:42px;height:42px}
  .phone__number{font-size:48px;font-weight:800;color:var(--white);letter-spacing:-.5px}

  .headline{position:absolute;left:36px;top:208px;line-height:1}
  .headline__lead{display:block;font-size:34px;font-weight:900;color:var(--brand-red)}
  .headline__sub{display:block;font-size:36px;font-weight:400;color:var(--brand-blue);margin-top:2px}

  .services{position:absolute;top:288px;list-style:none}
  .services--left{left:33px}
  .services--right{left:234px}
  .services li{position:relative;padding-left:32px;font-size:22px;line-height:29px;color:var(--ink-dark)}
  .services li::before{content:"";position:absolute;left:0;top:6px;width:18px;height:18px;border-radius:50%;background:var(--brand-red)}
  .services li::after{content:"";position:absolute;left:4px;top:11px;width:6px;height:6px;border-top:2px solid var(--white);border-right:2px solid var(--white);transform:rotate(45deg)}

  .visit{position:absolute;left:535px;top:520px;width:350px;text-align:center}
  .visit__icon{width:34px;height:34px;display:block;margin:0 auto 4px}
  .visit__label{display:block;font-size:21px;color:var(--accent-pink)}
  .visit__url{display:block;font-size:26px;font-weight:800;color:var(--white);margin-top:2px}
</style>
</head>
<body>

<!-- Option 1 -->
<div class="ad-frame ad-frame--one">
  <section class="ad">
    <svg class="ad__bg" viewBox="0 0 917 636">
      <defs>
        <linearGradient id="photo-one" x1="0" x2="1" y1="0" y2="0">
          <stop offset="0" stop-color="#ffffff"/>
          <stop offset=".25" stop-color="#f1f0ea"/>
          <stop offset=".5" stop-color="#dcd9cc"/>
          <stop offset=".72" stop-color="#d6c36a"/>
          <stop offset="1" stop-color="#c9c4b2"/>
        </linearGradient>
        <linearGradient id="c-drone" x1="0" y1="0" x2="0" y2="1"><stop offset="0" stop-color="#5c7a4a"/><stop offset="1" stop-color="#3f5a30"/></linearGradient>
        <linearGradient id="c-cockpit" x1="0" y1="0" x2="1" y2="1"><stop offset="0" stop-color="#4d6f96"/><stop offset="1" stop-color="#2a2f3a"/></linearGradient>
        <linearGradient id="c-jet" x1="0" y1="0" x2="0" y2="1"><stop offset="0" stop-color="#8aa4c4"/><stop offset="1" stop-color="#3a4a60"/></linearGradient>
      </defs>
      <rect x="330" y="100" width="587" height="440" fill="url(#photo-one)" role="img" aria-label="Photo of a yellow rescue helicopter in flight against a cloudy sky"/>
      <path d="M0,0 H917 V140 C820,120 640,125 470,160 C330,190 150,190 0,140 Z" fill="var(--brand-blue)"/>
      <path d="M0,140 C150,190 330,190 470,160 C640,125 820,120 917,140" fill="none" stroke="var(--white)" stroke-width="8"/>
      <path d="M0,0 H917 V100 C820,90 640,100 470,140 C330,175 150,165 0,98 Z" fill="var(--brand-red)"/>
      <path d="M0,0 V88 C60,140 200,165 300,152 C400,138 460,60 480,0 Z" fill="var(--white)"/>
      <rect x="480" y="18" width="437" height="62" rx="31" fill="var(--brand-red-dark)"/>
      <rect x="880" y="18" width="37" height="62" fill="var(--brand-red-dark)"/>
      <path d="M0,470 C250,545 480,520 640,500 C760,485 850,480 917,490 V525 C820,515 720,520 600,545 C420,580 200,580 0,505 Z" fill="var(--brand-red)"/>
      <path d="M0,505 C200,580 420,580 600,545 C720,520 820,515 917,525 V636 H0 Z" fill="var(--brand-blue)"/>
      <circle cx="122" cy="528" r="88" fill="url(#c-drone)" stroke="var(--brand-red)" stroke-width="8" role="img" aria-label="Photo of a white quadcopter drone over grass"/>
      <circle cx="293" cy="532" r="80" fill="url(#c-cockpit)" stroke="var(--brand-red)" stroke-width="8" role="img" aria-label="Photo of a pilot in a flight simulator cockpit"/>
      <circle cx="452" cy="522" r="73" fill="url(#c-jet)" stroke="var(--brand-red)" stroke-width="8" role="img" aria-label="Photo of an airliner parked at an airport gate"/>
    </svg>

    <div class="brand"><span class="brand__mark"></span><span class="brand__name">Pelterane Aviation</span></div>

    <div class="phone">
      <svg class="phone__icon" viewBox="0 0 42 42"><circle cx="21" cy="21" r="18" fill="none" stroke="#fff" stroke-width="3"/><path d="M14,12 l4,-1 3,6 -3,2 c1,3 3,5 6,6 l2,-3 6,3 -1,4 c-9,1 -17,-7 -17,-17 z" fill="#fff"/></svg>
      <span class="phone__number">(02) 4931 7262</span>
    </div>

    <h2 class="headline"><span class="headline__lead">Specialist Aviation</span><span class="headline__sub">Insurance Brokers</span></h2>

    <ul class="services services--left"><li>Fixedwing</li><li>Rotorwing</li><li>MROs</li><li>Manufacturers</li></ul>
    <ul class="services services--right"><li>Drones</li><li>Loss of Licence</li><li>Personal Accident</li></ul>

    <div class="visit">
      <svg class="visit__icon" viewBox="0 0 34 34" fill="none" stroke="#6f86c4" stroke-width="2"><circle cx="17" cy="17" r="14"/><ellipse cx="17" cy="17" rx="6" ry="14"/><line x1="3" y1="17" x2="31" y2="17"/><path d="M6,9 H28 M6,25 H28"/></svg>
      <span class="visit__label">Visit Us</span>
      <span class="visit__url">www.qmvaviation.com.au</span>
    </div>
  </section>
</div>
<p class="option-label option-label--one">Sample 1</p>

<!-- Option 2 -->
<div class="ad-frame ad-frame--two">
  <section class="ad">
    <svg class="ad__bg" viewBox="0 0 917 636">
      <defs>
        <linearGradient id="photo-two" x1="0" x2="1" y1="0" y2="0">
          <stop offset="0" stop-color="#ffffff"/>
          <stop offset=".2" stop-color="#eef0ea"/>
          <stop offset=".45" stop-color="#8a9c7c"/>
          <stop offset=".7" stop-color="#c9cdc6"/>
          <stop offset="1" stop-color="#4c6640"/>
        </linearGradient>
        <linearGradient id="c-heli" x1="0" y1="0" x2="0" y2="1"><stop offset="0" stop-color="#8a8a80"/><stop offset="1" stop-color="#e0a23a"/></linearGradient>
        <linearGradient id="c-cockpit2" x1="0" y1="0" x2="1" y2="1"><stop offset="0" stop-color="#4d6f96"/><stop offset="1" stop-color="#2a2f3a"/></linearGradient>
        <linearGradient id="c-jet2" x1="0" y1="0" x2="0" y2="1"><stop offset="0" stop-color="#8aa4c4"/><stop offset="1" stop-color="#3a4a60"/></linearGradient>
      </defs>
      <rect x="330" y="100" width="587" height="440" fill="url(#photo-two)" role="img" aria-label="Photo of a white quadcopter drone hovering above green grass"/>
      <path d="M0,0 H917 V140 C820,120 640,125 470,160 C330,190 150,190 0,140 Z" fill="var(--brand-blue)"/>
      <path d="M0,140 C150,190 330,190 470,160 C640,125 820,120 917,140" fill="none" stroke="var(--white)" stroke-width="8"/>
      <path d="M0,0 H917 V100 C820,90 640,100 470,140 C330,175 150,165 0,98 Z" fill="var(--brand-red)"/>
      <path d="M0,0 V88 C60,140 200,165 300,152 C400,138 460,60 480,0 Z" fill="var(--white)"/>
      <rect x="480" y="18" width="437" height="62" rx="31" fill="var(--brand-red-dark)"/>
      <rect x="880" y="18" width="37" height="62" fill="var(--brand-red-dark)"/>
      <path d="M0,470 C250,545 480,520 640,500 C760,485 850,480 917,490 V525 C820,515 720,520 600,545 C420,580 200,580 0,505 Z" fill="var(--brand-red)"/>
      <path d="M0,505 C200,580 420,580 600,545 C720,520 820,515 917,525 V636 H0 Z" fill="var(--brand-blue)"/>
      <circle cx="122" cy="528" r="88" fill="url(#c-heli)" stroke="var(--brand-red)" stroke-width="8" role="img" aria-label="Photo of a yellow helicopter against a sunset sky"/>
      <circle cx="293" cy="532" r="80" fill="url(#c-cockpit2)" stroke="var(--brand-red)" stroke-width="8" role="img" aria-label="Photo of a pilot in a flight simulator cockpit"/>
      <circle cx="452" cy="522" r="73" fill="url(#c-jet2)" stroke="var(--brand-red)" stroke-width="8" role="img" aria-label="Photo of an airliner parked at an airport gate"/>
    </svg>

    <div class="brand"><span class="brand__mark"></span><span class="brand__name">Pelterane Aviation</span></div>

    <div class="phone">
      <svg class="phone__icon" viewBox="0 0 42 42"><circle cx="21" cy="21" r="18" fill="none" stroke="#fff" stroke-width="3"/><path d="M14,12 l4,-1 3,6 -3,2 c1,3 3,5 6,6 l2,-3 6,3 -1,4 c-9,1 -17,-7 -17,-17 z" fill="#fff"/></svg>
      <span class="phone__number">(02) 4931 7262</span>
    </div>

    <h2 class="headline"><span class="headline__lead">Specialist Aviation</span><span class="headline__sub">Insurance Brokers</span></h2>

    <ul class="services services--left"><li>Fixedwing</li><li>Rotorwing</li><li>MROs</li><li>Manufacturers</li></ul>
    <ul class="services services--right"><li>Drones</li><li>Loss of Licence</li><li>Personal Accident</li></ul>

    <div class="visit">
      <svg class="visit__icon" viewBox="0 0 34 34" fill="none" stroke="#6f86c4" stroke-width="2"><circle cx="17" cy="17" r="14"/><ellipse cx="17" cy="17" rx="6" ry="14"/><line x1="3" y1="17" x2="31" y2="17"/><path d="M6,9 H28 M6,25 H28"/></svg>
      <span class="visit__label">Visit Us</span>
      <span class="visit__url">www.qmvaviation.com.au</span>
    </div>
  </section>
</div>
<p class="option-label option-label--two">Sample 2</p>

</body>
</html>
```